Fresh, modern, fun business card for pediatric dental practice

Need a business card for fresh, modern, fun pediatric dental practice

Clean look that matches our website's font and colors

We prefer the look of curved corners on business cards

Target Market(s)

parents (mothers) of young children, professionals, mid-high class

Industry/Entity Type

Dental

Contact Information for Business Card

Maplebrook Pediatric Dentistry
482 Orchard Vale Road
Suite 517
Alder Falls, PA 17000
555.419.3067
www.maplebrookkidsdental.example

Mara Tevlin, DMD
Colette Varnum, DMD
(we are working on our email address, but we would like that on the card as well)

Font styles to use
Sans Serif

Requirements
Must have
• All info; we would also like to make cards for individual staff members
• colors from our website and color palatte, attatched
• use same font and design as website for branding
Nice to have
• clean, simple card that has a pop of color
• we would like to see a few designs with our tag line "where smiles get brighter"
• we are not sure if we want to have it on there or not
• we would like to see a few designs incorporating the ribbon graphic on our website where the word WELCOME is

```html
<!DOCTYPE html>
<html lang="en">
<head>
<meta charset="utf-8">
<title>Maplebrook Pediatric Dentistry – Business Card</title>
<link href="https://fonts.googleapis.com/css2?family=Open+Sans:wght@400;600;700&display=swap" rel="stylesheet">
<style>
  :root {
    --plum: #4e2447;
    --magenta: #c4378b;
    --sun: #efb12b;
    --rose: #d9848f;
    --paper: #ffffff;
    --mist: #e9e6e8;
    --stage: #2b2b2d;
    --ink: #3d2a3a;
  }
  * { box-sizing: border-box; margin: 0; padding: 0; }
  html, body { width: 1200px; height: 900px; overflow: hidden; }
  body {
    background: var(--stage);
    font-family: "Open Sans", sans-serif;
    position: relative;
  }
  .card {
    position: absolute;
    width: 700px;
    height: 390px;
    left: 250px;
    border-radius: 28px;
    overflow: hidden;
    background: var(--paper);
  }
  .card--front { top: 40px; background: var(--plum); }
  .card--back { top: 470px; }
  .block { position: absolute; }

  /* front */
  .front-plum-left { left: 0; top: 0; width: 160px; height: 140px; background: var(--plum); }
  .front-magenta-left { left: 0; top: 140px; width: 160px; height: 102px; background: var(--magenta); }
  .front-sun { left: 0; top: 242px; width: 700px; height: 148px; background: var(--sun); }
  .front-plum-right { right: 0; top: 0; width: 200px; height: 98px; background: var(--plum); }
  .front-magenta-right { right: 0; top: 98px; width: 200px; height: 78px; background: var(--magenta); }
  .front-sun-right { right: 0; top: 176px; width: 200px; height: 66px; background: var(--sun); }
  .welcome-panel {
    left: 140px; top: 20px; width: 410px; height: 300px;
    background: var(--paper);
    box-shadow: 0 4px 14px rgba(0,0,0,.18);
    display: flex; flex-direction: column; align-items: center; justify-content: center;
    gap: 26px;
  }
  .welcome-label {
    font-size: 15px; letter-spacing: 9px; color: var(--ink); font-weight: 400;
  }
  .brand {
    display: flex; align-items: center; gap: 14px;
  }
  .brand-dot { width: 40px; height: 40px; border-radius: 50%; background: var(--sun); flex: none; }
  .brand-name {
    color: var(--magenta); font-weight: 700; line-height: 1.05;
  }
  .welcome-panel .brand-name { font-size: 30px; }

  /* back */
  .back-mist { right: 0; top: 0; width: 56px; height: 190px; background: var(--mist); }
  .back-sun { left: 0; top: 200px; width: 462px; height: 78px; background: var(--sun); }
  .back-rose { left: 462px; top: 170px; width: 78px; height: 62px; background: var(--rose); }
  .back-magenta { left: 540px; top: 140px; width: 160px; height: 92px; background: var(--magenta); }
  .back-plum { left: 0; top: 278px; width: 700px; height: 112px; background: var(--plum); }
  .back-plum-right { left: 462px; top: 232px; width: 238px; height: 60px; background: var(--plum); }
  .back-brand { left: 40px; top: 55px; }
  .back-brand .brand-name { font-size: 34px; }
  .address {
    left: 470px; top: 40px; font-size: 14px; line-height: 1.35; color: var(--ink); font-weight: 600;
  }
  .doctor {
    left: 40px; top: 222px; display: flex; align-items: center; gap: 10px;
    font-size: 25px; color: var(--plum);
  }
  .doctor strong { font-weight: 700; }
  .doctor span { font-weight: 400; }
  .icon { flex: none; }
  .contacts {
    left: 44px; top: 290px; list-style: none; color: var(--paper); font-size: 19px; line-height: 28px;
  }
  .contacts li { display: flex; align-items: center; gap: 12px; }
  .plane { right: 40px; top: 252px; }
</style>
</head>
<body>

<section class="card card--front" aria-label="Card front">
  <div class="block front-plum-left"></div>
  <div class="block front-magenta-left"></div>
  <div class="block front-sun"></div>
  <div class="block front-plum-right"></div>
  <div class="block front-magenta-right"></div>
  <div class="block front-sun-right"></div>
  <div class="block welcome-panel">
    <p class="welcome-label">WELCOME TO</p>
    <div class="brand">
      <span class="brand-dot"></span>
      <p class="brand-name">Maplebrook<br>Pediatric Dentistry</p>
    </div>
  </div>
</section>

<section class="card card--back" aria-label="Card back">
  <div class="block back-mist"></div>
  <div class="block back-magenta"></div>
  <div class="block back-rose"></div>
  <div class="block back-sun"></div>
  <div class="block back-plum-right"></div>
  <div class="block back-plum"></div>

  <div class="block brand back-brand">
    <span class="brand-dot"></span>
    <p class="brand-name">Maplebrook<br>Pediatric Dentistry</p>
  </div>

  <p class="block address">482 Orchard Vale Road<br>Suite 517<br>Alder Falls, PA 17000</p>

  <p class="block doctor">
    <svg class="icon" width="26" height="26" viewBox="0 0 26 26" aria-hidden="true">
      <circle cx="13" cy="13" r="13" fill="var(--magenta)"/>
      <circle cx="13" cy="10" r="4" fill="#fff"/>
      <path d="M6 20c1.5-4 4-5 7-5s5.5 1 7 5z" fill="#fff"/>
    </svg>
    <span class="doctor-name"><strong>Colette Varnum</strong><span>, DMD</span></span>
  </p>

  <ul class="block contacts">
    <li>
      <svg class="icon" width="22" height="22" viewBox="0 0 22 22" aria-hidden="true">
        <circle cx="11" cy="11" r="10" fill="none" stroke="var(--sun)" stroke-width="1.6"/>
        <path d="M7 6.5l2 .3 1 2.4-1.3 1a6 6 0 0 0 3 3l1-1.3 2.4 1 .3 2c-4.5.8-9.2-3.9-8.4-8.4z" fill="var(--sun)"/>
      </svg>
      555.419.3067
    </li>
    <li>
      <svg class="icon" width="22" height="22" viewBox="0 0 22 22" aria-hidden="true">
        <circle cx="11" cy="11" r="10" fill="none" stroke="var(--sun)" stroke-width="1.6"/>
        <rect x="6" y="7.5" width="10" height="7" fill="var(--sun)"/>
        <path d="M6 7.5l5 4 5-4" fill="none" stroke="var(--plum)" stroke-width="1"/>
      </svg>
      colette@maplebrookkidsdental.example
    </li>
    <li>
      <svg class="icon" width="22" height="22" viewBox="0 0 22 22" aria-hidden="true">
        <circle cx="11" cy="11" r="10" fill="none" stroke="var(--sun)" stroke-width="1.6"/>
        <circle cx="11" cy="11" r="5.5" fill="none" stroke="var(--sun)" stroke-width="1.2"/>
        <path d="M5.5 11h11M11 5.5v11" stroke="var(--sun)" stroke-width="1"/>
      </svg>
      www.maplebrookkidsdental.example
    </li>
  </ul>

  <svg class="block plane" width="44" height="40" viewBox="0 0 44 40" aria-hidden="true">
    <path d="M2 18L42 2 32 36 20 26z M20 26l22-24 M20 26v12l6-7" fill="none" stroke="var(--sun)" stroke-width="1.8" stroke-linejoin="round"/>
  </svg>
</section>

</body>
</html>
```